Domainer Needs a Wordpress Company Website

I need a wordpress design for a new small business in Portland, Or called Tulvex .com . I want to put the growing collection of virtual real estate /domains online for sale to end-users, small businesses, and other local stakeholders. Basically a portfolio website with cashlume link for immediate payment and then confirmed info is returned to Owner:Tulvex, Inc..

I would like to use previously purchased roster of wordpress plugins from QX Lantern.net that would incorporate into this company design. Some of the plugins to spread the word and social media concerns. It would be zipped file to you of course.

I do have a collection of wordpress themes from BrisklyMotifs.com that are interesting. If interested.

Basically, I need someone to take the pieces I supply and make a wordpress website thats allows cashlume payments. A couple of forms to be sent. A website that allows me to list the virtual properties and accepts potential clients request for more information and/or their payments to cashlume for a domain.
Im committed to : white space on all pages. html5 complied . cashlume. , listing several 100's domains to sell on this handcrafted website of yours.

Target Market(s)

mom and pop local business, local and regional businesses, end users, marketing agency, marketing groups, product groups, national producers,
Professionals. Clients. Teachers and students. Domainers.

Industry/Entity Type

Real Estate

Font styles to use
Sans Serif

Colors
f78f20
f68e4e
fabb94
f04a50
00a98f
ffffff

Requirements
Must have
• Company website. Easy to look at, easy to read.
Instilling projecting that professionals are behind this website.
Class. Exclusive maybe.
Pages: home, who are we, domains, contact, faq, blog, .
Cashlume link. Confirmation page to Tulvex, Inc stating payment for said domain or hosting.

White Space , Gold , gold muted , type colors. Greens. Shades of Blues
Should not have
• Dark pages.
Sloppy pages.
Pages that don't shift synchronize.
non professionalism looks or outdated photos, models, fonts.

```html
<!DOCTYPE html>
<html lang="en">
<head>
<meta charset="utf-8">
<title>Tulvex.com — Web Hosting</title>
<link href="https://fonts.googleapis.com/css2?family=Roboto+Condensed:wght@400;700&family=Open+Sans:wght@400;600;700&display=swap" rel="stylesheet">
<style>
:root{
  --orange:#f78f20;
  --peach:#f68e4e;
  --peach-light:#fabb94;
  --red:#f04a50;
  --teal:#00a98f;
  --white:#ffffff;
  --ink:#333333;
  --muted:#666666;
  --dark:#4a4a4a;
  --footer:#2b2b2b;
  --footer-deep:#1f1f1f;
}
*{margin:0;padding:0;box-sizing:border-box}
html,body{width:727px;height:1200px;overflow:hidden;background:var(--white)}
body{font-family:"Open Sans",sans-serif;color:var(--ink);font-size:7px;position:relative}
.section{position:absolute;left:0;width:727px}

/* top bar */
.topbar{top:0;height:26px;border-top:2px solid var(--teal)}
.topbar .contact{position:absolute;left:110px;top:8px;font-size:7px;display:flex;gap:14px;align-items:center}
.topbar .contact span{display:flex;align-items:center;gap:4px}
.lang{position:absolute;left:531px;top:0;width:60px;height:17px;background:var(--teal);color:#fff;font-size:7px;display:flex;align-items:center;justify-content:center;gap:4px}
.lang .flag{width:10px;height:7px;background:#fff;position:relative}
.lang .flag::before{content:"";position:absolute;left:4px;top:0;width:2px;height:7px;background:var(--red)}
.lang .flag::after{content:"";position:absolute;left:0;top:2.5px;width:10px;height:2px;background:var(--red)}
.search{position:absolute;left:597px;top:0;width:20px;height:17px;background:var(--teal)}

/* header */
.header{top:26px;height:42px;background:var(--orange)}
.brand{position:absolute;left:110px;top:7px;font-family:"Roboto Condensed",sans-serif;font-size:26px;color:#fff;letter-spacing:-.3px}
.nav{position:absolute;left:260px;top:12px;display:flex;gap:4px;font-size:8px;font-family:"Roboto Condensed",sans-serif}
.nav a{color:#333;text-decoration:none;padding:3px 6px}
.nav a.active{background:var(--teal);color:#fff}
.auth{position:absolute;left:535px;top:12px;display:flex;align-items:center;font-size:8px;font-weight:700}
.auth .login{background:var(--teal);color:#fff;padding:3px 8px}
.auth .or{width:12px;height:12px;border-radius:50%;background:var(--orange);color:#fff;font-size:5px;display:flex;align-items:center;justify-content:center;margin:0 -3px;position:relative;z-index:1;border:1px solid #fff}
.auth .help{background:var(--peach-light);color:#fff;padding:3px 10px}

/* hero */
.hero{top:68px;height:268px;background:linear-gradient(180deg,#f2f2f2,#fafafa 70%,#fff)}
.hero .portrait{position:absolute;left:0;top:0;width:230px;height:230px;background:linear-gradient(160deg,#d8d8d8,#a99486 55%,#3a3a3a)}
.hero .equipment{position:absolute;left:420px;top:110px;width:300px;height:140px;background:linear-gradient(90deg,#222 0%,#2a3b55 45%,#e8e8e8 60%,#e6c84a 75%,#d94d4d 88%,#f2f2f2)}
.hero .clouds{position:absolute;left:0;top:210px;width:727px;height:58px}
.bubble{position:absolute;left:228px;top:66px;width:188px;height:188px;border-radius:50%;background:var(--red);color:#fff;font-family:"Roboto Condensed",sans-serif;font-size:18px;line-height:25.5px;text-align:center;display:flex;align-items:center;justify-content:center}
.bubble-small{position:absolute;left:373px;top:186px;width:72px;height:72px;border-radius:50%;background:var(--orange);color:#fff;font-size:7px;line-height:11px;text-align:center;display:flex;align-items:center;justify-content:center;border:2px solid #fff;z-index:2}

/* support strip */
.support{top:336px;height:78px}
.support .phone-icon{position:absolute;left:110px;top:16px}
.support .num{position:absolute;left:151px;top:18px;font-size:13px;font-style:italic;color:var(--orange);font-weight:600}
.support .phone-text{position:absolute;left:151px;top:35px;width:200px;font-size:6.3px;line-height:10px}
.support .chat-icon{position:absolute;left:389px;top:18px}
.support .chat-text{position:absolute;left:445px;top:18px;width:175px;font-size:6.3px;line-height:10px}
.btn-teal{background:var(--teal);color:#fff;font-size:7px;font-weight:600;padding:3px 7px;display:inline-block}
.support .chat-btn{position:absolute;left:445px;top:44px}

/* features band */
.features{top:414px;height:178px;background:linear-gradient(90deg,#d9d9d9,#efefef 30%,#efefef 70%,#d9d9d9)}
.tabs{position:absolute;left:110px;top:15px;display:flex;gap:6px}
.tab{background:var(--orange);color:#333;font-family:"Roboto Condensed",sans-serif;font-weight:700;font-size:9px;padding:4px 10px;height:21px}
.tab.current{background:#fff;color:var(--orange);font-weight:400}
.tab-panel{position:absolute;left:110px;top:36px;width:339px;height:140px;display:flex}
.tab-panel .feature{width:113px;background:#fff;display:flex;flex-direction:column;align-items:center;padding-top:28px;color:var(--teal);font-size:8.5px;font-weight:600;gap:10px}
.tab-panel .copy{flex:1;background:#cfcfcf;padding:12px 10px;font-size:6.3px;line-height:11px;color:#444}
.tab-panel .copy .btn-teal{margin-top:10px;font-size:6.5px}
.domain{position:absolute;left:466px;top:15px;width:151px;height:162px;background:var(--peach);color:#fff;padding:8px 10px}
.domain h3{font-family:"Roboto Condensed",sans-serif;font-weight:400;font-size:12px}
.domain .hint{margin-top:11px;font-size:6.8px}
.domain .field{margin-top:8px;height:17px;background:var(--peach-light)}
.check{display:inline-flex;align-items:center;gap:3px;font-size:6.5px}
.check i{width:6px;height:6px;background:#fff;display:inline-block;position:relative}
.check i::after{content:"";position:absolute;left:1.5px;top:0;width:2px;height:4px;border:solid var(--peach);border-width:0 1px 1px 0;transform:rotate(40deg)}
.domain .all{margin-top:8px}
.tlds{margin-top:12px;display:grid;grid-template-columns:repeat(3,auto);gap:5px 6px;width:95px}
.btn-red{background:var(--red);color:#fff;font-size:7.5px;padding:3px 7px;display:inline-block;margin-top:7px}

/* pricing */
.customers{top:604px;left:110px;width:507px}
.section-title{font-family:"Roboto Condensed",sans-serif;font-size:12px;color:var(--red);font-weight:400}
.customers p{margin-top:5px;font-size:6.3px;line-height:10.5px;color:#555}
.plans{top:654px;left:110px;width:507px;display:flex;justify-content:space-between}
.plan{width:153px;height:240px;border:2px solid;background:#fff}
.plan.standard{border-color:var(--orange)}
.plan.premium{border-color:var(--red)}
.plan.pro{border-color:var(--teal)}
.plan .name{background:var(--dark);color:#fff;font-family:"Roboto Condensed",sans-serif;font-size:15px;text-align:center;height:28px;line-height:28px;border-bottom:1px solid #666}
.plan .price{background:var(--dark);height:34px;text-align:center;font-family:"Roboto Condensed",sans-serif;font-size:14px;line-height:34px;position:relative}
.plan .price::after{content:"";position:absolute;left:50%;bottom:-5px;margin-left:-5px;border:5px solid transparent;border-bottom:0;border-top-color:var(--dark)}
.plan .price small{font-size:7px;color:#999;font-family:"Open Sans",sans-serif}
.standard .price{color:var(--orange)}
.premium .price{color:var(--red)}
.pro .price{color:var(--teal)}
.plan ul{list-style:none;margin-top:6px}
.plan li{height:15.2px;line-height:15.2px;text-align:center;font-size:6px;color:#444}
.plan li:nth-child(even){background:#f2f2f2}

/* testimonials */
.testimonials{top:906px;left:110px;width:332px}
.slider{position:absolute;right:0;top:3px;display:flex;gap:1px}
.slider span{width:10px;height:10px;display:flex;align-items:center;justify-content:center}
.slider .prev{background:var(--dark)}
.slider .next{background:var(--red)}
.quote{position:relative;height:60px}
.quote.first{margin-top:12px}
.quote .avatar{position:absolute;left:0;top:0;width:50px;height:44px;background:linear-gradient(160deg,#eee,#b9a79c 55%,#2d2d2d)}
.quote .body{position:absolute;left:56px;top:0;width:270px}
.quote .lead{color:var(--teal);font-size:7px}
.quote .lead b{font-family:Georgia,serif;font-size:11px;color:var(--ink);margin-right:4px}
.quote .text{margin-top:3px;font-size:6.3px;line-height:10px;color:#555}
.quote .by{margin-top:4px;font-style:italic;font-size:6.8px;color:var(--red)}

.newsletter{top:909px;left:465px;width:152px;height:127px;padding:4px}
.newsletter .frame{position:absolute;inset:0;border:4px dashed var(--red);border-right-color:#aaa;border-bottom-color:#aaa}
.newsletter .inner{position:absolute;inset:4px;background:#fff;padding:8px 10px}
.newsletter h3{font-family:"Roboto Condensed",sans-serif;color:var(--teal);font-weight:400;font-size:12.5px;padding-bottom:3px;border-bottom:1px solid #cfe}
.newsletter p{margin-top:6px;font-size:6.5px;line-height:10.5px}
.newsletter .email{margin-top:8px;border:1px solid #ddd;height:17px;font-size:6px;color:#aaa;padding:4px 5px}
.newsletter .sub{margin-top:8px;background:var(--orange);color:#fff;font-size:7.5px;font-weight:600;padding:4px 8px;display:inline-block}
.newsletter .paper{position:absolute;right:10px;bottom:8px}

/* footer */
.footer{top:1056px;height:124px;background:var(--footer)}
.footer .col{position:absolute;top:16px}
.footer h4{font-family:"Roboto Condensed",sans-serif;font-weight:400;font-size:9.5px;color:var(--teal)}
.footer ul{list-style:none;margin-top:13px}
.footer .links li{font-size:6.3px;color:#999;height:13px}
.footer .links li::before{content:"≡";margin-right:3px;font-size:5px}
.footer .links li.on{color:var(--orange)}
.footer .info li{font-size:6.3px;color:#999;height:18px;display:flex;gap:4px;line-height:8px}
.footer .form .in{width:107px;height:13px;border:1px solid #555;margin-top:3px;font-size:5px;color:#888;padding:2px 5px;font-style:italic}
.footer .form .in.msg{height:28px}
.footer .form .send{margin-top:5px;background:var(--peach-light);color:#333;font-size:6.8px;font-weight:700;padding:2px 6px;display:inline-block}
.cards{display:flex;flex-direction:column;gap:5px;margin-top:9px;align-items:flex-end}
.cards span{width:27px;height:15px;border-radius:2px;font-size:5.5px;font-weight:600;display:flex;align-items:center;justify-content:center;color:#333}
.copyright{top:1180px;height:20px;background:var(--footer-deep);color:#999;font-size:6.3px;text-align:center;line-height:20px}
.copyright b{color:#ccc;font-weight:400}
</style>
</head>
<body>

<header class="section topbar">
  <div class="contact">
    <span><svg width="7" height="7" viewBox="0 0 10 10"><path d="M2 6V5a3 3 0 0 1 6 0v1" fill="none" stroke="#333" stroke-width="1.4"/><rect x="1" y="5.5" width="2" height="3" fill="#333"/><rect x="7" y="5.5" width="2" height="3" fill="#333"/></svg>014 552 8031</span>
    <span><svg width="7" height="7" viewBox="0 0 10 10"><path d="M1 1h8v5H4L2 8V6H1z" fill="#333"/></svg>Live chat</span>
  </div>
  <div class="lang"><span class="flag"></span>English ▾</div>
  <div class="search"><svg width="20" height="17" viewBox="0 0 20 17"><circle cx="11" cy="7" r="3.2" fill="none" stroke="#fff" stroke-width="1.4"/><path d="M8.7 9.3 6 12" stroke="#fff" stroke-width="1.6"/></svg></div>
</header>

<div class="section header">
  <div class="brand">Tulvex.com</div>
  <nav class="nav">
    <a class="active" href="#">Home</a><a href="#">Who are we</a><a href="#">Domains</a><a href="#">Faq's</a><a href="#">Blog</a><a href="#">Contact Us</a>
  </nav>
  <div class="auth"><span class="login">Login</span><span class="or">or</span><span class="help">Help</span></div>
</div>

<section class="section hero">
  <div class="portrait" role="img" aria-label="Photo of a smiling professional woman at her desk"></div>
  <div class="equipment" role="img" aria-label="Illustration of server towers and a cup of coloured pencils"></div>
  <svg class="clouds" viewBox="0 0 727 58" preserveAspectRatio="none" aria-hidden="true">
    <path d="M0 30 Q30 5 65 22 Q95 0 135 20 Q165 8 190 24 Q230 10 260 30 L260 58 L0 58Z M440 40 Q480 18 520 32 Q560 12 600 30 Q640 14 680 28 Q705 20 727 26 L727 58 L440 58Z" fill="#fff"/>
    <rect x="0" y="40" width="727" height="18" fill="#fff"/>
  </svg>
  <div class="bubble">Web Hosting<br>Should be Easy.<br>We make sure<br>that its so easy<br>a child could</div>
  <div class="bubble-small">Lorem ipsum<br>dolor sit amet,<br>consectetur<br>adipiscing elit.</div>
</section>

<section class="section support">
  <svg class="phone-icon" width="28" height="42" viewBox="0 0 28 42" aria-hidden="true">
    <path d="M10 4 H4 Q0 4 0 9 V33 Q0 38 4 38 H10 V28 H6 V14 H10Z" fill="var(--orange)"/>
    <path d="M15 15 Q19 21 15 27 M19 11 Q26 21 19 31" fill="none" stroke="var(--orange)" stroke-width="2.5"/>
  </svg>
  <div class="num">0149 552 803</div>
  <div class="phone-text">Available by phone, email, Web, even Chirpline. We are here for you, feel free to reach out. Our staff is extremely skilled</div>
  <svg class="chat-icon" width="42" height="38" viewBox="0 0 42 38" aria-hidden="true">
    <path d="M21 2C10 2 1 9 1 18c0 9 9 16 20 16 3 0 5-.4 7-1l10 4-3-8c4-3 6-7 6-11C41 9 32 2 21 2z" fill="var(--teal)"/>
    <circle cx="13" cy="18" r="2.8" fill="#fff"/><circle cx="21" cy="18" r="2.8" fill="#fff"/><circle cx="29" cy="18" r="2.8" fill="#fff"/>
  </svg>
  <div class="chat-text">We are available 24/7 to answer your questions. We specialize in customer service.</div>
  <span class="btn-teal chat-btn">Live Chat</span>
</section>

<section class="section features">
  <div class="tabs">
    <span class="tab current">Hosting</span><span class="tab">Our Security</span><span class="tab">Our Speed</span><span class="tab">Affiliates</span>
  </div>
  <div class="tab-panel">
    <div class="feature">
      <svg width="36" height="30" viewBox="0 0 36 30" aria-hidden="true">
        <path d="M9 28 Q1 28 1 21 Q1 14 8 14 Q9 6 17 6" fill="none" stroke="var(--teal)" stroke-width="3"/>
        <path d="M19 6 Q27 6 28 13 Q35 13 35 21 Q35 28 27 28 Z" fill="none" stroke="var(--teal)" stroke-width="3"/>
        <path d="M9 28 H27" stroke="var(--teal)" stroke-width="3"/>
        <path d="M15 0h6v9h5l-8 8-8-8h5z" fill="var(--teal)"/>
        <circle cx="14" cy="22" r="1.5" fill="var(--teal)"/><circle cx="18" cy="22" r="1.5" fill="var(--teal)"/><circle cx="22" cy="22" r="1.5" fill="var(--teal)"/>
      </svg>
      Cloud Hosting
    </div>
    <div class="copy">
      Lorem ipsum dolor sit amet, consectetur adipiscing elit. Sed non leo et est mattis viverra a non lectus. Donec sit amet eros consequat, venenatis lorem at, mattis felis. Lorem ipsum dolor siet, consectetur adipiscing elit. Phasellus scelerisque elit sem, vel tempus lorem feugiat non. Lorem ipsum dolor sit amet, consectetur adipiscing elit. Class aptent taciti sociosqu ad litora torquent per conubia nostra, per inceptos himenaeos. Phasellus et sapien odio.<br>
      <span class="btn-teal">Read more »</span>
    </div>
  </div>
  <div class="domain">
    <h3>Domain Checker</h3>
    <div class="hint">Enter a domain to check below :</div>
    <div class="field"></div>
    <div class="check all"><i></i>Check All Domain Types</div>
    <div class="tlds">
      <span class="check"><i></i>.com</span><span class="check"><i></i>.net</span><span class="check"><i></i>.info</span>
      <span class="check"><i></i>.org</span><span class="check"><i></i>.co.uk</span><span class="check"><i></i>.edu</span>
    </div>
    <span class="btn-red">Check Domain</span>
  </div>
</section>

<section class="section customers">
  <h2 class="section-title">Our Customers Love Our Work</h2>
  <p>Lorem ipsum dolor sit amet, consectetur adipiscing elit. Sed non leo et est mattis viverra a non lectus. Donec sit amet eros consequat, venenatis lorem at, mattis felis. Lorem ipsum dolor sit amet, consectetur adipiscing elit. Phasellus scelerisque elit sem, vel tempus lorem feugiat non. Lorem ipsum dolor sit amet.</p>
</section>

<section class="section plans">
  <div class="plan standard">
    <div class="name">Standard</div>
    <div class="price">Free!</div>
    <ul>
      <li>Fully functional scheduling tool</li><li>Filters for easy viewing</li><li>Web Based: Login Anywhere</li><li>Track students &amp; instructors</li><li>Store/access Customer Info</li><li>Notekeeping &amp; Attendance</li><li>SSL security</li><li>Regular data backups</li><li>1 User account</li><li>E-mail support</li><li>No Credit Card Required</li>
    </ul>
  </div>
  <div class="plan premium">
    <div class="name">Premium</div>
    <div class="price">$39 <small>/ month</small></div>
    <ul>
      <li>3 User Accounts</li><li>Simultaneous Logins</li><li>Collaboration: File Sharing &amp; Storage</li><li>Activity Feed: Track your efforts</li><li>Activity Feed: Discussion Board</li><li>Reports: Attendance Sheets</li><li>Reports: Instructor Work Histories &amp; Schedules</li><li>Reports: Customer Histories &amp; Schedules</li><li>Best in Class Phone Support</li>
    </ul>
  </div>
  <div class="plan pro">
    <div class="name">Professional</div>
    <div class="price">$79 <small>/ month</small></div>
    <ul>
      <li>Powerful Point of Sale System</li><li>Accept Credit Cards Immediately</li><li>Web Store: Sell Your Classes Online</li><li>Easily Publish Your Schedule Online</li><li>Sell Retail Goods, Tickets, and More</li><li>SteadyReach Integration</li><li>LedgerNest Integration</li><li>Add User Accounts for $5</li><li>Priority Customer Support</li>
    </ul>
  </div>
</section>

<section class="section testimonials">
  <h2 class="section-title">Testimonials</h2>
  <div class="slider">
    <span class="prev"><svg width="5" height="6" viewBox="0 0 5 6"><path d="M4 0 0 3l4 3z" fill="#fff"/></svg></span>
    <span class="next"><svg width="5" height="6" viewBox="0 0 5 6"><path d="M1 0l4 3-4 3z" fill="#fff"/></svg></span>
  </div>
  <div class="quote first">
    <div class="avatar" role="img" aria-label="Portrait photo of the reviewer"></div>
    <div class="body">
      <div class="lead"><b>“</b>Lorem ipsum dolor sit amet</div>
      <div class="text">Lorem ipsum dolor sit amet, consectetur adipiscinglit. Donec nec dignissim lorem. Vestibulum lesuada ac auctor vitae, mollis tempus dolor quat ”</div>
      <div class="by">Posed by &nbsp;Mira Holten (President and Chief Software Architect)</div>
    </div>
  </div>
  <div class="quote">
    <div class="avatar" role="img" aria-label="Portrait photo of the reviewer"></div>
    <div class="body">
      <div class="lead"><b>“</b>Lorem ipsum dolor sit amet</div>
      <div class="text">Lorem ipsum dolor sit amet, consectetur adipiscinglit. Donec nec dignissim lorem. Vestibulum lesuada ac auctor vitae, mollis tempus dolor quat ”</div>
      <div class="by">Posed by &nbsp;Mira Holten (President and Chief Software Architect)</div>
    </div>
  </div>
</section>

<aside class="section newsletter">
  <div class="frame"></div>
  <div class="inner">
    <h3>Newsletter</h3>
    <p>Fill out the below form to stay up to date with the lates news</p>
    <div class="email">Enter your email</div>
    <span class="sub">Subscribe</span>
    <svg class="paper" width="34" height="30" viewBox="0 0 34 30" aria-hidden="true">
      <rect x="4" y="2" width="28" height="26" fill="none" stroke="var(--red)" stroke-width="2"/>
      <path d="M4 10H0v16a2 2 0 0 0 4 2" fill="none" stroke="var(--red)" stroke-width="2"/>
      <rect x="9" y="6" width="18" height="6" fill="var(--red)"/>
      <path d="M9 16h18M9 20h18M9 24h18" stroke="var(--red)" stroke-width="2"/>
    </svg>
  </div>
</aside>

<footer class="section footer">
  <div class="col" style="left:110px">
    <h4>Link</h4>
    <ul class="links"><li class="on">Home</li><li>Who are we</li><li>Domains</li><li>Faq's</li><li>Blog</li><li>Contact Us</li></ul>
  </div>
  <div class="col" style="left:225px">
    <h4>Get in Touch</h4>
    <ul class="info">
      <li><svg width="6" height="8" viewBox="0 0 6 8"><path d="M2 0H0v8h2V6H1V2h1z" fill="var(--orange)"/></svg>(+07) 418 552 8031</li>
      <li><svg width="8" height="6" viewBox="0 0 8 6"><rect width="8" height="6" fill="var(--orange)"/><path d="M0 0l4 3 4-3" fill="none" stroke="#2b2b2b"/></svg>support@tulvex .com</li>
      <li><svg width="7" height="7" viewBox="0 0 8 8"><circle cx="4" cy="4" r="3.4" fill="none" stroke="var(--orange)"/><path d="M0.6 4h6.8M4 .6v6.8" stroke="var(--orange)" stroke-width=".7"/></svg>www.Tulvex .com</li>
      <li><svg width="6" height="8" viewBox="0 0 6 8"><path d="M3 8 0.5 4A3 3 0 1 1 5.5 4z" fill="var(--orange)"/><circle cx="3" cy="3" r="1" fill="#2b2b2b"/></svg>Lorem ipsum dolor sit amet,<br>rices tortor - 123456</li>
    </ul>
  </div>
  <div class="col form" style="left:395px">
    <h4>Get in Touch</h4>
    <div style="margin-top:8px">
      <div class="in">Name</div><div class="in">Email</div><div class="in msg">Message</div>
      <span class="send">Submit</span>
    </div>
  </div>
  <div class="col" style="left:560px;width:57px;text-align:right">
    <h4>Payment</h4>
    <div class="cards">
      <span style="background:#fff">Vantra</span>
      <span style="background:#fff">Cashlume</span>
      <span style="background:var(--peach-light)">Merilo</span>
      <span style="background:#f3df6a">Dexopay</span>
    </div>
  </div>
</footer>
<div class="section copyright">Copyright © 2014 Tulvex .com. All Rights Reserved. | <b>Legal</b> | <b>Privacy</b></div>

</body>
</html>
```